K & K Fabrications Brochure

We need a 2 page (front and back) full color brochure for our Mechanical Contracting company. The website is http://www.kkfabrications.example although we're looking for something fresh. If anything the future web design might follow the design of this brochure more than we'd like to have the brochure follow the design of the website. However, to start please use content found on the website and we will refine. We want basically a cover, 2 inner pages and a back. Attached is a an example brochure from another company as well as an outdated brochure we used previously.

Target Market(s)

1. Industrial, Commercial and Institutional Builders and Owners

2. Industrial, Commercial and Institutional HVAC Service customers

Industry/Entity Type

It Company

Font styles to use
Serif
Sans Serif

Requirements
Must have
• Strong imagery
Should not have
• Plumbing Service
Pictures of people besides Owner Oren Walczak and President Tomas Lindqvist

```html
<!DOCTYPE html>
<html lang="en">
<head>
<meta charset="utf-8">
<title>K &amp; K Fabrications Brochure – Inside Spread</title>
<link href="https://fonts.googleapis.com/css2?family=PT+Serif:ital,wght@0,400;0,700;1,400;1,700&display=swap" rel="stylesheet">
<style>
  :root{
    --blue:#0b5aab;
    --blue-dark:#0a4a8f;
    --paper:#ffffff;
    --lavender:#dfe3f2;
    --grey-band:#8a8a8a;
    --grey-box:#a9a9a9;
    --ink:#1d1d1d;
    --backdrop:#6f6f6f;
  }
  *{box-sizing:border-box;margin:0;padding:0}
  html,body{width:1200px;height:1000px;overflow:hidden}
  body{background:var(--backdrop);font-family:"PT Serif",Georgia,serif;color:var(--ink)}
  .spread{position:absolute;left:40px;top:110px;width:1120px;height:760px;background:var(--paper);overflow:hidden;box-shadow:0 6px 20px rgba(0,0,0,.35)}
  .spine{position:absolute;left:560px;top:0;width:1px;height:100%;background:rgba(0,0,0,.12)}
  .abs{position:absolute}
  .top-bars div{position:absolute;background:var(--blue);left:50%;transform:translateX(-50%)}
  .rule{position:absolute;height:2px;background:var(--blue)}
  .tab{position:absolute;background:var(--blue);color:#fff;font-weight:700;font-size:16px;padding:3px 10px 4px;border-radius:4px 4px 0 0;line-height:1.2}
  .tab.small{font-size:14px}
  .body-text{font-size:11px;line-height:1.3;text-align:justify}
  .body-text p+p{margin-top:9px}
  .photo{position:absolute;border:2px solid var(--blue);border-radius:8px}
  .band-promise{position:absolute;left:0;width:560px;top:288px;height:132px;background:var(--lavender);border-top:2px solid var(--blue);border-bottom:2px solid var(--blue)}
  .promise-lead{color:var(--blue);font-style:italic;font-weight:700;font-size:10.5px;margin:14px 38px 10px 38px}
  .promise-text{font-size:10px;line-height:1.35;margin:0 20px 0 38px;text-align:justify}
  .band-grey{position:absolute;top:478px;height:268px;background:var(--grey-band);border-bottom:3px solid var(--blue)}
  .bullets{list-style:none;position:absolute}
  .bullets li{position:relative;padding-left:20px;font-size:11px;font-weight:700;height:24.3px}
  .bullets li::before{content:"";position:absolute;left:0;top:2px;width:11px;height:11px;border-radius:50%;background:var(--blue)}
  .skew-photo{position:absolute;border:2px solid #fff;border-radius:12px;transform:skewX(-6deg)}
  .services-title{position:absolute;left:580px;top:60px;width:520px;display:flex;align-items:center;justify-content:center;gap:6px;color:var(--blue);font-weight:700;font-size:15px}
  .services{list-style:none;position:absolute;left:582px;top:102px}
  .services li{display:flex;align-items:center;gap:8px;font-size:15px;height:29.5px}
  .staff-bio{position:absolute;left:660px;top:486px;width:460px;height:70px;background:var(--grey-box);font-size:10.5px;line-height:1.3;padding:2px 10px 0 8px;text-align:justify}
  .staff-list{list-style:none;position:absolute}
  .staff-list li{position:relative;padding-left:16px;font-size:10.5px;height:18.5px;color:#fff}
  .staff-list li b{font-weight:700}
  .staff-list li::before{content:"";position:absolute;left:0;top:2px;width:10px;height:10px;border-radius:50%;background:var(--blue)}
</style>
</head>
<body>
<main class="spread">
  <div class="spine"></div>

  <div class="top-bars">
    <div style="top:0;width:530px;height:22px"></div>
    <div style="top:28px;width:576px;height:12px"></div>
    <div style="top:46px;width:644px;height:9px"></div>
    <div style="top:60px;width:710px;height:5px"></div>
  </div>

  <!-- Left page: About us -->
  <div class="tab" style="left:40px;top:36px">About us</div>
  <div class="rule" style="left:0;top:66px;width:1120px"></div>

  <div class="abs body-text" style="left:38px;top:92px;width:298px">
    <p>100 years of service in the heating, cooling and plumbing industry has taught K &amp; K Fabrications to do the job right, the first time. Our DraftPro CAD capabilities deliver instantaneous design changes and enable K &amp; K to provide value engineering whenever necessary.</p>
    <p>In House sheet metal and pipefitting operations provide K &amp; K with the ability to deliver materials that match the quality of our workmanship.</p>
    <p>Our work history, experienced staff and in-house facilities make K &amp; K Fabrications well-suited for any project.</p>
  </div>
  <div class="photo" role="img" aria-label="Photo of rooftop mechanical units on a city building" style="left:355px;top:112px;width:186px;height:134px;background:linear-gradient(160deg,#b9c3cc 0%,#c9b7a0 55%,#8d8a80 100%)"></div>

  <!-- Our Promise -->
  <div class="tab" style="left:40px;top:262px">Our Promise</div>
  <section class="band-promise">
    <p class="promise-lead">K &amp; K Fabrications' continued dedication and commitment to quality, value and safety is vital to our success</p>
    <p class="promise-text">K &amp; K Fabrications, Inc. strives to be the best at serving our customers in all aspects of their mechanical and plumbing construction needs. Our customers rely on our expertise in design and construction to provide them with safe, reliable, and efficient mechanical systems. Our goal is to be quality, cost and safety conscious at all times and we recognize that our customers are the most valuable and important asset we have.</p>
  </section>

  <!-- Our Experience -->
  <div class="band-grey" style="left:0;width:560px"></div>
  <div class="tab" style="left:40px;top:452px">Our Experience</div>
  <ul class="bullets" style="left:40px;top:492px">
    <li>Alder County - courthouse</li>
    <li>Brookvale Hospital - Atrium</li>
    <li>Elm St. - Residence Hall</li>
    <li>Hartwell Center</li>
    <li>St. Agnes Hospital - Pinecrest</li>
    <li>Riverton Hospital</li>
    <li>North Ridge Prison</li>
    <li>Metro Switching Station</li>
    <li>State Central Campus Improvements</li>
    <li>Oakmont College</li>
  </ul>
  <div class="skew-photo" role="img" aria-label="Photo of a modern hospital building with a glass entrance" style="left:350px;top:482px;width:188px;height:100px;background:linear-gradient(180deg,#9cc3ea 0%,#d8e2ea 50%,#8f9aa3 100%)"></div>
  <div class="skew-photo" role="img" aria-label="Photo of a domed capitol building against a blue sky" style="left:282px;top:594px;width:190px;height:104px;background:linear-gradient(180deg,#5d97d6 0%,#a8c6e4 45%,#d9d6cc 70%,#6f8a5a 100%)"></div>

  <!-- Right page: services -->
  <div class="services-title">
    <svg width="26" height="22" viewBox="0 0 26 22" aria-hidden="true"><path d="M14 2 5 11l9 9M23 2l-9 9 9 9" fill="none" stroke="var(--blue)" stroke-width="4"/></svg>
    <span>Complete Mechanical Contracting Services</span>
    <svg width="26" height="22" viewBox="0 0 26 22" aria-hidden="true"><path d="M3 2l9 9-9 9M12 2l9 9-9 9" fill="none" stroke="var(--blue)" stroke-width="4"/></svg>
  </div>
  <ul class="services">
    <li><svg width="26" height="22" viewBox="0 0 26 22" aria-hidden="true"><path d="M2 1h9l11 10-11 10H2l11-10z" fill="var(--blue)"/></svg>Heating</li>
    <li><svg width="26" height="22" viewBox="0 0 26 22" aria-hidden="true"><path d="M2 1h9l11 10-11 10H2l11-10z" fill="var(--blue)"/></svg>Cooling</li>
    <li><svg width="26" height="22" viewBox="0 0 26 22" aria-hidden="true"><path d="M2 1h9l11 10-11 10H2l11-10z" fill="var(--blue)"/></svg>Sheet Metal</li>
    <li><svg width="26" height="22" viewBox="0 0 26 22" aria-hidden="true"><path d="M2 1h9l11 10-11 10H2l11-10z" fill="var(--blue)"/></svg>In house DraftPro CAD</li>
    <li><svg width="26" height="22" viewBox="0 0 26 22" aria-hidden="true"><path d="M2 1h9l11 10-11 10H2l11-10z" fill="var(--blue)"/></svg>Plan /Spec &amp; Design / Build</li>
  </ul>
  <div class="photo" role="img" aria-label="Photo of a large duct section being lifted through a warehouse door" style="left:848px;top:102px;width:240px;height:162px;border-width:3px;border-radius:12px;background:linear-gradient(90deg,#2f2f2f 0%,#7d7f82 35%,#c9cdd0 55%,#6b6d70 80%,#2a2a2a 100%)"></div>

  <div class="tab small" style="left:578px;top:264px">Sheet Metal Fabrication Facility</div>
  <div class="rule" style="left:560px;top:288px;width:560px"></div>
  <div class="abs" role="img" aria-label="Panoramic photo of the sheet metal fabrication shop floor" style="left:560px;top:308px;width:560px;height:86px;background:linear-gradient(180deg,#c7ccd0 0%,#8e969c 40%,#6b7882 70%,#a59a8a 100%)"></div>
  <div class="rule" style="left:0;top:416px;width:1120px"></div>

  <!-- Our Staff -->
  <div class="band-grey" style="left:560px;width:560px"></div>
  <div class="tab" style="left:578px;top:440px;padding-left:30px;padding-right:30px">Our Staff</div>
  <div class="abs" role="img" aria-label="Portrait photo of owner and CEO Oren Walczak" style="left:582px;top:482px;width:74px;height:78px;border:3px solid var(--blue);border-radius:4px;background:linear-gradient(180deg,#b9b4ad 0%,#7a6f66 60%,#2d2d33 100%)"></div>
  <div class="staff-bio">As owner and CEO, Oren oversees all operations at K &amp; K Fabrications. With 14 years experience in Mechanical Contracting and a steamfitter by trade, Oren has worked hard to improve quality control. Oren also is a Project Manager for several of K &amp; K's most important projects and serves on multiple boards and committees related to the industry.</div>
  <div class="abs" style="left:582px;top:564px;font-size:10.5px;font-weight:700">Oren Walczak – CEO</div>

  <ul class="staff-list" style="left:584px;top:586px">
    <li><b>Lars Henning</b>, President Emeritus</li>
    <li><b>Tomas Lindqvist</b>, Vice President</li>
    <li><b>Ned Voss</b>, Project Manager</li>
    <li><b>Rob Eckhart</b>, Project Manager</li>
    <li><b>Glen Harmer</b>, Project Manager</li>
    <li><b>Walt Brenner</b>, PE Industrial Project Manager</li>
  </ul>
  <ul class="staff-list" style="left:828px;top:586px">
    <li><b>Dean Kowal</b>, PE, Plumbing Department Manager</li>
    <li><b>Cole Varga</b>, DraftPro CAD Program Manager</li>
    <li><b>Tim Ostrander</b>, Sheet Metal Shop Foreman</li>
    <li><b>Ray Dettinger</b>, Chief Estimator</li>
    <li><b>Phil Marquardt</b>, Design Engineer</li>
    <li><b>Jon Pelham</b>, Service Manager</li>
  </ul>
</main>
</body>
</html>
```